Corvid Aviation - Learn to Fly

Our customers are people who span all ages and genders that are interested in learning how to fly airplanes for fun or as a career, or who would like to advance their piloting skills.

Flight training we offer:
Private Pilot Certificate
Instrument Rating
Commercial Pilot Certificate
Sport Pilot Certificate: Powered Parachute
Drone Pilot Training

Ground School we offer:
Sport Pilot Ground School
Private Pilot Ground School
Instrument Pilot Ground School
Drone Pilot Ground School

Target Market(s)

Bessemer, Alabama, United States: High school students, college students, career changers. Someone interested in learning to fly for fun or for a career in the United States.

Industry/Entity Type

Aviation

Requirements
Must have
• I would like for you to enjoy some creative freedom here. The feeling and image we want to portray is a professional, but also very exciting and energizing image. The prospective customer and student should see the brochure and be excited to call us or come out for more information on learning how to fly. Our tag line is: "Small Step Today, Giant Leap Tomorrow."
Nice to have
• It would be helpful if you can do some reading or a little research on each of the types of training that we offer so that you will understand what should be included in the brochure. Our goal is to let everyone know who we are, what we offer, and how to contact us.

This may help some with design ideas: The name Corvid Aviation is inspired by the Orbix Skyward space program because the owner of the flight school is a big fan of Orbix and the Skyward mission.

```html
<!DOCTYPE html>
<html lang="en">
<head>
<meta charset="utf-8">
<title>Corvid Aviation – Learn to Fly</title>
<link href="https://fonts.googleapis.com/css2?family=Barlow:wght@300;600;700&family=Barlow+Condensed:wght@600;700&display=swap" rel="stylesheet">
<style>
  :root {
    --page-bg: #e9e9e9;
    --navy: #111c33;
    --navy-deep: #0b1326;
    --red: #e3232c;
    --white: #ffffff;
    --sky-top: #f1dcc8;
    --sky-mid: #ead5bf;
    --sky-low: #e9a98f;
    --sky-horizon: #e88f77;
  }
  * { box-sizing: border-box; margin: 0; padding: 0; }
  html, body { width: 1102px; height: 1200px; overflow: hidden; }
  body { background: var(--page-bg); position: relative; font-family: "Barlow", sans-serif; }

  .flyer {
    position: absolute; left: 155px; top: 40px; width: 792px; height: 1120px;
    overflow: hidden;
    background: radial-gradient(circle at 22% 16%, #f8eee2 0%, transparent 38%),
      linear-gradient(180deg, var(--sky-top) 0%, var(--sky-mid) 38%, var(--sky-low) 62%, var(--sky-horizon) 75%);
    box-shadow: 0 6px 24px rgba(0,0,0,.15);
  }

  .brand {
    position: absolute; left: 25px; top: 45px; width: 290px; height: 290px;
    border: 6px solid var(--red); border-radius: 50%;
    display: flex; align-items: center; justify-content: center;
  }
  .brand-name {
    font-family: "Barlow", sans-serif; font-weight: 700; font-size: 38px;
    color: var(--navy); text-transform: uppercase; text-align: center; line-height: 1.1;
  }

  .offer-panel {
    position: absolute; left: 405px; top: 0; width: 340px;
    background: linear-gradient(180deg, var(--navy) 0%, var(--navy-deep) 100%);
    border-bottom-right-radius: 80px;
    padding: 56px 24px 44px 38px;
    font-family: "Barlow Condensed", sans-serif;
  }
  .offer-title {
    color: var(--red); font-weight: 700; font-size: 30px; line-height: 1.05;
    text-transform: uppercase; margin-bottom: 14px;
  }
  .offer-list { list-style: none; margin-bottom: 24px; }
  .offer-list:last-child { margin-bottom: 0; }
  .offer-list li {
    color: var(--white); font-weight: 600; font-size: 23px; line-height: 1.4;
    padding-left: 22px; position: relative;
  }
  .offer-list li::before {
    content: ""; position: absolute; left: 0; top: 11px;
    width: 11px; height: 11px; border-radius: 50%; background: var(--white);
  }

  .tagline { position: absolute; left: 34px; top: 405px; }
  .tagline .accent {
    display: block; color: var(--red); font-weight: 700; font-size: 48px;
    line-height: 1; text-transform: uppercase; letter-spacing: .5px;
  }
  .tagline .main {
    display: block; color: var(--navy); font-weight: 300; font-size: 118px;
    line-height: .95; text-transform: uppercase; margin-bottom: 10px;
  }

  .photo {
    position: absolute; left: 0; top: 720px; width: 792px; height: 260px;
    background: linear-gradient(180deg, rgba(232,143,119,0) 0%, #6d6b5b 30%, #3e5a2c 55%, #2e2e2e 80%, #262626 100%);
  }

  .footer-band { position: absolute; left: 0; top: 860px; width: 792px; height: 260px; }

  .contact {
    position: absolute; left: 0; right: 0; top: 1020px; text-align: center;
    color: var(--white); font-weight: 600; font-size: 38px; letter-spacing: .3px;
  }
</style>
</head>
<body>
  <main class="flyer">
    <div class="brand"><span class="brand-name">Corvid<br>Aviation</span></div>

    <section class="offer-panel">
      <h2 class="offer-title">Flight Training<br>We Offer:</h2>
      <ul class="offer-list">
        <li>Private Pilot Certificate</li>
        <li>Instrument Rating</li>
        <li>Commercial Pilot Certificate</li>
        <li>Sport Pilot Certificate</li>
        <li>Powered Parachute</li>
        <li>Drone Pilot Training</li>
      </ul>
      <h2 class="offer-title">Ground School<br>We Offer:</h2>
      <ul class="offer-list">
        <li>Sport Pilot Ground School</li>
        <li>Private Pilot Ground School</li>
        <li>Instrument Pilot Ground School</li>
        <li>Drone Pilot Ground School</li>
      </ul>
    </section>

    <div class="photo" role="img" aria-label="Photo of a small white training airplane on a runway at sunset, with grass and trees behind"></div>

    <h1 class="tagline">
      <span class="accent">Small Step</span>
      <span class="main">Today</span>
      <span class="accent">Giant Leap</span>
      <span class="main">Tomorrow</span>
    </h1>

    <svg class="footer-band" viewBox="0 0 792 260" preserveAspectRatio="none" aria-hidden="true">
      <path d="M0 112 Q400 90 792 28 L792 260 L0 260 Z" fill="#111c33"/>
      <path d="M0 112 Q400 90 792 28" fill="none" stroke="#e3232c" stroke-width="9"/>
    </svg>

    <p class="contact">Ph: 0198 765 4320 | www.corvidaviation.com</p>
  </main>
</body>
</html>
```